Corvath Partners is a boutique consultancy focused on CXO-level advisory on strategy, operations, and organization in the Consumer Packaged Goods and Retail sector.

Our typical clients are senior level executives (Typically SVP level or higher), who hire us to help solve strategic business challenges. Our consultants are typically charged out at very high rates (Typically $2,000 - $3,000 per day), therefore, our business cards need to convey a high end, classy, yet professional image, consistent with high value strategic consulting.

We would like to see designs and colors that convey excellence, competence, and growth.

Our name 'Corvath' is derived from the Native American name of Mt. McKinley, the highest peak in North America. We would like to have a logo on our business card, that is simple yet conveys the aspirational nature of what we offer, i.e enabling the achievement of high performance.

Boutique

Corvath Partners, LLC
4718 Brennock Avenue Northwest, Suite 640
Washington, District of Columbia, 20093
United States
Mobile: +1 202 555 0143
elira.voss@corvathpartnersllc.com

```html
<!DOCTYPE html>
<html lang="en">
<head>
<meta charset="utf-8">
<title>Corvath Partners – Business Card</title>
<link rel="stylesheet" href="https://fonts.googleapis.com/css2?family=Open+Sans:wght@400;600;700&display=swap">
<style>
  :root {
    --navy: #0d3a52;
    --navy-deep: #0a2f43;
    --orange: #f4511e;
    --paper: #f7f7f7;
    --paper-shade: #dcdcdc;
    --ink: #2b2b2b;
    --backdrop: #c3c8cf;
    --white: #ffffff;
  }
  html, body {
    margin: 0;
    padding: 0;
    width: 1200px;
    height: 866px;
    overflow: hidden;
    background: var(--backdrop);
    font-family: "Open Sans", Arial, sans-serif;
  }
  .canvas {
    position: relative;
    width: 1200px;
    height: 866px;
  }
  .card {
    position: absolute;
    width: 540px;
    height: 310px;
    overflow: hidden;
    box-shadow: 0 6px 18px rgba(0,0,0,0.18);
  }
  .card--back {
    left: 70px;
    top: 140px;
    background: var(--navy);
    display: flex;
    align-items: center;
    justify-content: center;
  }
  .card--front {
    left: 590px;
    top: 410px;
    background: radial-gradient(circle at 45% 50%, var(--white) 0%, var(--paper) 45%, var(--paper-shade) 100%);
  }
  .card__sweep {
    position: absolute;
    top: 0;
    right: 0;
    width: 196px;
    height: 100%;
    background: linear-gradient(160deg, var(--navy) 0%, var(--navy-deep) 100%);
  }
  .wordmark {
    margin: 0;
    font-weight: 600;
    letter-spacing: 0.04em;
    text-transform: uppercase;
  }
  .card--back .wordmark {
    color: var(--white);
    font-size: 34px;
  }
  .card--front .wordmark {
    position: absolute;
    left: 40px;
    top: 112px;
    color: var(--navy);
    font-size: 24px;
  }
  .holder {
    position: absolute;
    left: 40px;
    top: 182px;
  }
  .holder__name {
    margin: 0;
    color: var(--orange);
    font-weight: 700;
    font-size: 16px;
  }
  .holder__role {
    margin: 2px 0 0;
    color: var(--ink);
    font-size: 15px;
  }
  .contact {
    position: absolute;
    right: 20px;
    top: 150px;
    margin: 0;
    padding: 0;
    list-style: none;
    text-align: right;
    color: var(--white);
    font-size: 11.5px;
    line-height: 17px;
  }
  .contact__icon {
    display: inline-block;
    width: 10px;
    height: 10px;
    margin-left: 4px;
    vertical-align: -1px;
  }
</style>
</head>
<body>
<main class="canvas">

  <section class="card card--back" aria-label="Card back">
    <p class="wordmark">Corvath Partners</p>
  </section>

  <section class="card card--front" aria-label="Card front">
    <div class="card__sweep" role="img" aria-label="Decorative navy and orange wave sweep"></div>

    <p class="wordmark">Corvath Partners</p>

    <div class="holder">
      <p class="holder__name">Maren Holt-Avery</p>
      <p class="holder__role">Consultant</p>
    </div>

    <ul class="contact">
      <li>214.9th floor.Hall</li>
      <li>Brennock Road WDC</li>
      <li>012 555 0147
        <svg class="contact__icon" viewBox="0 0 10 10" aria-hidden="true"><path fill="var(--orange)" d="M2,0 L4,2.5 L3,3.8 C3.8,5.4 4.8,6.4 6.2,7 L7.5,6 L10,8 L8.5,10 C4,9.6 0.4,6 0,1.5 Z"/></svg>
      </li>
      <li>012 555 0147
        <svg class="contact__icon" viewBox="0 0 10 10" aria-hidden="true"><rect x="0" y="3" width="10" height="6" fill="var(--orange)"/><rect x="2.5" y="0.5" width="5" height="3" fill="var(--orange)"/></svg>
      </li>
      <li>maren@corvath.com
        <svg class="contact__icon" viewBox="0 0 10 10" aria-hidden="true"><rect x="0" y="2" width="10" height="7" fill="var(--orange)"/><path d="M0,2 L5,6 L10,2" fill="none" stroke="var(--navy)" stroke-width="1"/></svg>
      </li>
      <li>www.corvathpartners.com</li>
    </ul>
  </section>

</main>
</body>
</html>
```